independent cleaner, reliable, custom, thorough, trustworthy

Not sure yet if I want single-sided or double sided, so I'm selecting double-sided just in case, but single-sided designs are okay.

Really looking to find the happy medium between personal and professional in a business card design. I end up building comfortable relationships with the people I work for.

Most of my business is through referrals, but I want some business cards to hand out to people who ask for one (and maybe put them on community bulletin boards).

My target market is homeowners and business owners who are looking for a reliable cleaner and are willing to pay a bit more to have excellent quality and someone they trust.

Theme: I have a personal-professional feel since I'm solo, so the theme should reflect that. Trustworthy, personal, simple. I clean up messes.

Hopefully this is enough info, let me know if you have any questions though of course!

Target Market(s)

Homeowners businessowners who are looking for a reliable cleaner, excellent quality trustworthy.

Industry/Entity Type

Cleaning Service

Contact Information for Business Card

Please include this text:
• Delphine Marrow
• independent cleaner
• reliable, custom, thorough
• 604-317-2296
• tbw.marrow@quillpost.net

Font styles to use
Serif
Sans Serif

Colors
ffffff
00a990
0492cd
33a6d7
0355a3
3276b5
919191

Requirements
Must have
• Really looking to find the happy medium between personal and professional in a business card design.
• Background: at least 50% white on the side with the most text (coloured accents or shapes are okay)
• I lean more towards simple and clean, solid colours, maybe a gentle gradient
Nice to have
• Not sure yet if I want single-sided or double sided, so I'm selecting double-sided just in case, but single-sided designs are okay.
• Colours: preferably blues and teals for the font and other objects (if any). Open to designer's choice though. I've toyed around with orangey-yellow, but it doesn't feel right and I keep going back to blues/teals
• Also I uploaded a sketch of my signature and initials so you can get a feel for my personality. I'm not expecting this to be included in the design, it's just there.
Should not have
• I don't like a lot of busy-ness or textures
• Also I don't have a logo (not sure where else to specify this)

```html
<!DOCTYPE html>
<html lang="en">
<head>
<meta charset="utf-8">
<title>Delphine Marrow – Business Card</title>
<link href="https://fonts.googleapis.com/css2?family=Courgette&family=Lato:wght@400;700&family=Oswald:wght@500&display=swap" rel="stylesheet">
<style>
  :root {
    --white: #ffffff;
    --teal: #00a990;
    --blue: #0492cd;
    --grey: #919191;
    --ink: #222222;
    --backdrop: #2e2e2e;
  }
  html, body {
    margin: 0;
    padding: 0;
    width: 1200px;
    height: 1200px;
    overflow: hidden;
    background: var(--backdrop);
  }
  .canvas {
    position: relative;
    width: 1200px;
    height: 1200px;
  }
  .card {
    position: absolute;
    top: 310px;
    height: 594px;
    box-shadow: 0 4px 12px rgba(0,0,0,0.45);
    overflow: hidden;
  }
  .card-front {
    left: 234px;
    width: 364px;
    background: var(--white);
  }
  .card-back {
    left: 627px;
    width: 369px;
    background: var(--teal);
  }

  /* Front */
  .brand-mark {
    position: absolute;
    top: 440px;
    left: 0;
    width: 100%;
    display: flex;
    align-items: center;
    justify-content: center;
    gap: 10px;
    top: 130px;
    font-family: "Lato", sans-serif;
    font-weight: 700;
    font-size: 20px;
    color: var(--teal);
  }
  .brand-mark .dot {
    width: 16px;
    height: 16px;
    border-radius: 50%;
    background: var(--blue);
  }
  .owner-name {
    position: absolute;
    top: 230px;
    left: 0;
    width: 100%;
    text-align: center;
    font-family: "Courgette", cursive;
    font-size: 33px;
    color: var(--blue);
    margin: 0;
    line-height: 1;
  }
  .role {
    position: absolute;
    top: 269px;
    left: 40px;
    right: 42px;
    display: flex;
    align-items: center;
    gap: 6px;
    font-family: "Lato", sans-serif;
    font-size: 13px;
    letter-spacing: 0.2px;
    color: var(--grey);
    text-transform: uppercase;
    white-space: nowrap;
  }
  .role::before, .role::after {
    content: "";
    flex: 1;
    height: 1px;
    background: var(--grey);
  }
  .tagline {
    position: absolute;
    top: 296px;
    left: 0;
    width: 100%;
    text-align: center;
    font-family: "Lato", sans-serif;
    font-size: 18px;
    color: var(--ink);
  }
  .band {
    position: absolute;
    left: 0;
    width: 100%;
    display: flex;
    align-items: center;
    justify-content: center;
    color: var(--white);
  }
  .band-phone {
    top: 393px;
    height: 67px;
    background: var(--blue);
    font-family: "Oswald", sans-serif;
    font-weight: 500;
    font-size: 34px;
    letter-spacing: 0.5px;
  }
  .band-email {
    top: 472px;
    height: 81px;
    background: var(--teal);
    font-family: "Lato", sans-serif;
    font-size: 24px;
  }

  /* Back */
  .back-top {
    position: absolute;
    top: 0;
    left: 0;
    width: 100%;
    height: 290px;
    background: var(--blue);
  }
  .back-mark {
    position: absolute;
    top: 270px;
    left: 0;
    width: 100%;
    display: flex;
    align-items: center;
    justify-content: center;
    gap: 12px;
    font-family: "Lato", sans-serif;
    font-weight: 700;
    font-size: 30px;
    color: var(--white);
  }
  .back-mark .dot {
    width: 22px;
    height: 22px;
    border-radius: 50%;
    background: var(--white);
  }
</style>
</head>
<body>
<main class="canvas">
  <section class="card card-front" aria-label="Business card front">
    <div class="brand-mark"><span class="dot"></span>Delphine Marrow</div>
    <h1 class="owner-name">Delphine Marrow</h1>
    <div class="role">Independent Cleaner</div>
    <div class="tagline">Reliable | Custom | Thorough</div>
    <div class="band band-phone">604-317-2296</div>
    <div class="band band-email">tbw.marrow@quillpost.net</div>
  </section>

  <section class="card card-back" aria-label="Business card back">
    <div class="back-top"></div>
    <div class="back-mark"><span class="dot"></span>Delphine Marrow</div>
  </section>
</main>
</body>
</html>
```